Supplement Rebranding Bottle Design

READ WORD DOCUMENT ATTACHED.
We want to rebrand our current health supplements (see below). We do want it to be modern, vibrant and appealing. Very upscale and elegant as it targets primarily women.
Bottle size: see pictures for bottle size, along with sample bottles that we like; we’re open to any bottle similar to the ones attached.
Current bottles: So ideally, we’d keep the core color on each bottle with a new branding/bottle design. But we're open to your suggestion.

Target Market(s)

mostly women but shouldn't be overly feminine

Requirements
Must have
• see bottle sizes attached

```html
<!DOCTYPE html>
<html lang="en">
<head>
<meta charset="utf-8">
<title>Aurel Supplement Labels</title>
<link rel="stylesheet" href="https://fonts.googleapis.com/css2?family=Montserrat:wght@700&family=Archivo:wght@400;500&display=swap">
<style>
  :root {
    --bg-top: #ffffff;
    --bg-bottom: #ebebed;
    --glass: #d9dadc;
    --glass-edge: #cfd0d3;
    --neck: #cdced1;
    --ink: #ffffff;
    --liver-cap: #a35fc8;
    --liver-fill: #a88bc9;
    --tummy-cap: #c1302c;
    --tummy-fill: #b5605b;
    --hormone-cap: #2f8a3c;
    --hormone-fill: #6e9b78;
    --sugar-cap: #2a52c6;
    --sugar-fill: #7f98cc;
  }
  * { box-sizing: border-box; margin: 0; padding: 0; }
  html, body { width: 1200px; height: 807px; overflow: hidden; }
  body {
    background: linear-gradient(180deg, var(--bg-top) 0%, var(--bg-bottom) 100%);
    position: relative;
    font-family: "Archivo", Arial, sans-serif;
  }
  .bottle {
    position: absolute;
    top: 155px;
    width: 240px;
    height: 495px;
    color: var(--ink);
  }
  .bottle__cap {
    position: absolute;
    left: 28px;
    width: 197px;
    top: 0;
    height: 82px;
    border-radius: 8px 8px 4px 4px;
    background:
      repeating-linear-gradient(90deg, rgba(0,0,0,0.10) 0 2px, transparent 2px 7px),
      linear-gradient(90deg, rgba(0,0,0,0.12), rgba(255,255,255,0.12) 45%, rgba(0,0,0,0.12)),
      var(--cap);
  }
  .bottle__neck {
    position: absolute;
    left: 36px;
    width: 181px;
    top: 80px;
    height: 16px;
    background: var(--neck);
  }
  .bottle__body {
    position: absolute;
    left: 0;
    right: 0;
    top: 94px;
    bottom: 0;
    background: linear-gradient(90deg, var(--glass-edge), var(--glass) 20%, var(--glass) 80%, var(--glass-edge));
    border-radius: 70px 70px 14px 14px / 60px 60px 12px 12px;
    overflow: hidden;
  }
  .bottle__fill {
    position: absolute;
    left: 14px;
    right: 14px;
    top: 100px;
    bottom: 8px;
    background:
      radial-gradient(ellipse at 60% 40%, var(--fill) 0%, transparent 75%),
      linear-gradient(180deg, transparent 0%, var(--fill) 25%, var(--fill) 80%, transparent 100%);
    opacity: 0.9;
  }
  .bottle__text {
    position: absolute;
    left: var(--text-left);
    top: 0;
    right: 6px;
    bottom: 0;
  }
  .bottle__name {
    position: absolute;
    top: 196px;
    font-family: "Montserrat", Arial, sans-serif;
    font-weight: 700;
    font-size: 21px;
    letter-spacing: -0.6px;
    white-space: nowrap;
  }
  .bottle__claim {
    position: absolute;
    top: 290px;
    font-weight: 500;
    font-size: 11px;
    line-height: 14px;
    letter-spacing: 0.3px;
    text-transform: uppercase;
    white-space: nowrap;
  }
  .bottle__type {
    position: absolute;
    top: 364px;
    font-size: 8.5px;
    white-space: nowrap;
  }
  .bottle__count {
    position: absolute;
    top: 375px;
    font-size: 5px;
    font-weight: 500;
    white-space: nowrap;
  }
  .bottle__volume {
    position: absolute;
    top: 447px;
    font-size: 6px;
  }
  .bottle--liver   { left: 125px; --cap: var(--liver-cap);   --fill: var(--liver-fill);   --text-left: 27px; }
  .bottle--tummy   { left: 355px; --cap: var(--tummy-cap);   --fill: var(--tummy-fill);   --text-left: 15px; }
  .bottle--hormone { left: 583px; --cap: var(--hormone-cap); --fill: var(--hormone-fill); --text-left: 13px; }
  .bottle--sugar   { left: 809px; --cap: var(--sugar-cap);   --fill: var(--sugar-fill);   --text-left: 11px; }
</style>
</head>
<body>
  <main>
    <section class="bottle bottle--liver">
      <div class="bottle__cap"></div>
      <div class="bottle__neck"></div>
      <div class="bottle__body">
        <div class="bottle__fill" role="img" aria-label="Purple capsules seen through the bottle"></div>
      </div>
      <div class="bottle__text">
        <p class="bottle__name">LiverAurel</p>
        <p class="bottle__claim">Rejuvenating cleanse<br>&amp; detox formula</p>
        <p class="bottle__type">Dietary Supplement</p>
        <p class="bottle__count">120 Vegetable Capsules</p>
        <p class="bottle__volume">100 ml</p>
      </div>
    </section>
    <section class="bottle bottle--tummy">
      <div class="bottle__cap"></div>
      <div class="bottle__neck"></div>
      <div class="bottle__body">
        <div class="bottle__fill" role="img" aria-label="Red capsules seen through the bottle"></div>
      </div>
      <div class="bottle__text">
        <p class="bottle__name">Tummy Aurel</p>
        <p class="bottle__claim">Oxygenating colon<br>cleanse</p>
        <p class="bottle__type">Dietary Supplement</p>
        <p class="bottle__count">90 Vegetable Capsules</p>
        <p class="bottle__volume">100 ml</p>
      </div>
    </section>
    <section class="bottle bottle--hormone">
      <div class="bottle__cap"></div>
      <div class="bottle__neck"></div>
      <div class="bottle__body">
        <div class="bottle__fill" role="img" aria-label="Green capsules seen through the bottle"></div>
      </div>
      <div class="bottle__text">
        <p class="bottle__name">Hormone Aurel</p>
        <p class="bottle__claim">Supports healthy<br>hormone levels</p>
        <p class="bottle__type">Dietary Supplement</p>
        <p class="bottle__count">60 Vegetable Capsules</p>
        <p class="bottle__volume">100 ml</p>
      </div>
    </section>
    <section class="bottle bottle--sugar">
      <div class="bottle__cap"></div>
      <div class="bottle__neck"></div>
      <div class="bottle__body">
        <div class="bottle__fill" role="img" aria-label="Blue capsules seen through the bottle"></div>
      </div>
      <div class="bottle__text">
        <p class="bottle__name">Blood Sugar Aurel</p>
        <p class="bottle__claim">Supports healthy<br>blood glucose levels</p>
        <p class="bottle__type">Dietary Supplement</p>
        <p class="bottle__count">60 Vegetable Capsules</p>
        <p class="bottle__volume">100 ml</p>
      </div>
    </section>
  </main>
</body>
</html>
```